VLM Wellness Business Card

A Double Sided Business Card

I am a private company in Melbourne, Australia, working in the Health industry. I am a nutritionist and lifestyle coach, whom specialises in using raw foods ie. fruits/nuts/vegetables to help heal my clients and enable them to achieve their ultimate state of health.

I want a sophisticated design and colour for my card that appeals to both men and women from teenage through to elderly.

Front of Card:

Red apple peel spiral in the shape of an apple. I would like a leaf/leaves coming off the stem of the apple. Please see attachments for example.

***On Right Hand side of Image is business Name: VLM Wellness

Underneath LOGO use slogan " Let Food Be Your Medicine"

***Use Deep Red and Blues for Text Colouring

Back of Card:

Marisol Fenwick
Nutritional Specialist and Lifestyle Coach

Specialising in: Diseased Conditions
Weight Management
Achieving your Ultimate State of Health

enquiries@vlmwellness.example.au 0497 365 204

**Make sure the front design of the card flows onto the back.
Updates

Email address has been amended, Also more specific details have been given for apple peel Image, and another image attached as example of Leaf on stem of apple.

I little more insight into what sort of feel were trying to create. We're apart of the health industry, and we want the card to have a medical/clinical feeling about it.

Target Market(s)

Males and Females from teenages to elderly

Industry/Entity Type

Business

Requirements
Must have
• Red Apple Peel Spiral, in the shape of an apple, with a leaf/leaves attached to stem.
***Must be in the shape of an apple
***Please use coloring on inside of apple peel to resemble inside of an apple.
Nice to have
• I would like my card to have a clinical feel.
Should not have
• We don't want the image of the apple to look like a Christmas decoration

```html
<!DOCTYPE html>
<html lang="en">
<head>
<meta charset="utf-8">
<title>Marisol Fenwick – Business Card (Back)</title>
<link rel="stylesheet" href="https://fonts.googleapis.com/css2?family=Questrial&display=swap">
<style>
  :root {
    --ink-black: #0b0b0b;
    --paper: #ffffff;
    --mist: #e9e9ea;
    --silver: #c4c4c6;
    --name-red: #d52a2a;
    --accent-red: #c8201f;
    --heading-navy: #2b3a8c;
    --body-ink: #1d1d1f;
    --on-dark: #ffffff;
  }
  * { margin: 0; padding: 0; box-sizing: border-box; }
  html, body {
    width: 1200px; height: 741px; overflow: hidden;
    background: var(--paper);
  }
  .card {
    position: relative;
    width: 1200px; height: 741px; overflow: hidden;
    font-family: "Questrial", "Helvetica Neue", Arial, sans-serif;
    background: radial-gradient(ellipse at 60% 30%, var(--paper) 0%, var(--mist) 100%);
  }
  .card__ribbons { position: absolute; inset: 0; }
  .identity {
    position: absolute; left: 0; right: 0; top: 240px;
    text-align: center; color: var(--on-dark);
  }
  .identity__name {
    font-size: 52px; font-weight: 400; color: var(--name-red);
    line-height: 1.05; letter-spacing: 0.5px;
  }
  .identity__role {
    font-size: 37px; line-height: 1.12; letter-spacing: 0.8px; margin-top: 6px;
  }
  .services {
    position: absolute; left: 0; right: 0; top: 424px;
    text-align: center; color: var(--body-ink);
  }
  .services__heading {
    font-size: 38px; color: var(--heading-navy); line-height: 1.1;
  }
  .services__list {
    list-style: none; font-size: 33px; line-height: 1.3; margin-top: 2px;
  }
  .services__list li { display: inline; }
  .services__list li::before { content: "·"; margin-right: 2px; }
  .services__list li + li { margin-left: 22px; }
  .services__list .services__full { display: block; margin-left: 0; }
  .contact {
    position: absolute; left: 56px; top: 590px;
    list-style: none; color: var(--on-dark); font-size: 35px;
  }
  .contact__item { display: flex; align-items: center; height: 56px; }
  .contact__icon { width: 44px; height: 44px; margin-right: 14px; flex: none; }
  .apple-motif {
    position: absolute; left: 1005px; top: 560px;
    width: 150px; height: 150px; border-radius: 48% 48% 46% 46%;
    background: radial-gradient(circle at 40% 35%, #f05252 0%, var(--accent-red) 55%, #8f1414 100%);
  }
</style>
</head>
<body>
<main class="card">
  <svg class="card__ribbons" viewBox="0 0 1200 741" width="1200" height="741" aria-hidden="true">
    <defs>
      <linearGradient id="silver-ribbon" x1="0" y1="0" x2="1" y2="0">
        <stop offset="0" stop-color="#f4f4f4"/>
        <stop offset="0.5" stop-color="#bdbdbf"/>
        <stop offset="1" stop-color="#ececec"/>
      </linearGradient>
    </defs>
    <path d="M0,70 C300,40 700,60 1200,120 L1200,160 C760,110 340,100 0,140 Z" fill="url(#silver-ribbon)" opacity="0.7"/>
    <path d="M0,135 C320,150 720,200 1200,150 L1200,370 C880,400 560,430 0,320 Z" fill="var(--ink-black)"/>
    <path d="M0,470 C360,400 820,400 1200,350 L1200,395 C820,460 380,470 0,500 Z" fill="url(#silver-ribbon)"/>
    <path d="M0,545 C320,520 760,560 1200,480 L1200,520 C780,610 340,560 0,580 Z" fill="var(--silver)" opacity="0.8"/>
    <path d="M0,565 C320,545 760,585 1200,505 L1200,741 L0,741 Z" fill="var(--ink-black)"/>
  </svg>

  <header class="identity">
    <h1 class="identity__name">Marisol Fenwick</h1>
    <p class="identity__role">Nutritional Specialist<br>Lifestyle Coach</p>
  </header>

  <section class="services">
    <h2 class="services__heading">Specialising in:</h2>
    <ul class="services__list">
      <li>Diseased Conditions</li>
      <li>Weight Management</li>
      <li class="services__full">Achieving your Ultimate State of Health</li>
    </ul>
  </section>

  <ul class="contact">
    <li class="contact__item">
      <svg class="contact__icon" viewBox="0 0 44 44" aria-hidden="true">
        <circle cx="22" cy="22" r="21" fill="var(--accent-red)"/>
        <g fill="none" stroke="var(--on-dark)" stroke-width="2">
          <circle cx="22" cy="22" r="12"/>
          <ellipse cx="22" cy="22" rx="5" ry="12"/>
          <line x1="10" y1="22" x2="34" y2="22"/>
          <path d="M12,16 H32 M12,28 H32"/>
        </g>
      </svg>
      <span>enquiries@vlmwellness.example.au</span>
    </li>
    <li class="contact__item">
      <svg class="contact__icon" viewBox="0 0 44 44" aria-hidden="true">
        <circle cx="22" cy="22" r="21" fill="var(--accent-red)"/>
        <path d="M15,11 l5,0 l2,7 l-3,2 c1.5,3 3.5,5 6,6 l2,-3 l7,2 l0,5 c-1,2 -3,3 -5,3 c-9,-1 -16,-9 -17,-17 c0,-2 1,-4 3,-5 z" fill="var(--on-dark)"/>
      </svg>
      <span>0497 365 204</span>
    </li>
  </ul>

  <div class="apple-motif" role="img" aria-label="Red apple peel spiral shaped as an apple"></div>
</main>
</body>
</html>
```